Produktdesign - Kosmetikprodukt
Zielgruppe
Damen ab 50
Aufgabenstellung
Ausgeschrieben wird ein ansprechendes und hochwertiges Produktdesign für eine neu einzuführende Creme zur Vergrößerung der weiblichen Brust.
Produktname: soleva amarin
Verpackung: Weiße Tube mit Schraubverschluss
Zu verwendende Begriffe auf der Vorderseite:
- soleva amarin als edler Schriftzug
- VOLUME effect
- DETOX effect
- FIRMING effect
Zu verwendende Informationen auf der Rückseite:
Mit Dreifach-Wirkkomplex....
VOLUME effect: stimuliert die Adipozytendifferenzierung, damit
funktionsfähige Adipozyten entstehen - positiver Effekt auf Volumen
DETOX effect: Tessalin aktiviert Proteasome 20S, die beschädigte
Zellen beseitigt und so die Zelltoxizität herabsetzt.
FIRMING effect: steigert die Dynamik der Fibrolasten um die Matrix
Wechselwirkungen wiederherzustellen.
- Barcode mit EAN: 4019283746512
- Inhalt: 50ml
- Made in germany
- Kelbrand GmbH, Anton - Feiler - Str. 7, 34567 Musterdorf

```html
<!DOCTYPE html>
<html lang="de">
<head>
<meta charset="utf-8">
<title>soleva amarin – Tube Vorder- und Rückseite</title>
<link rel="stylesheet" href="https://fonts.googleapis.com/css2?family=Inconsolata:wght@400;500&family=Open+Sans:wght@400;700&display=swap">
<style>
  :root {
    --paper: #ffffff;
    --tube: #f6f6f6;
    --tube-edge: #e3e3e3;
    --cap: #eeeeee;
    --gold: #e6bd00;
    --ink: #1a1a1a;
  }
  html, body {
    margin: 0;
    padding: 0;
    overflow: hidden;
    background: var(--paper);
  }
  .canvas {
    position: relative;
    width: 1049px;
    height: 1200px;
    overflow: hidden;
    background: var(--paper);
  }
  .tube-shapes {
    position: absolute;
    inset: 0;
  }
  .block {
    position: absolute;
    text-align: center;
    margin: 0;
  }
  /* front */
  .brand-dot {
    position: absolute;
    left: 250px;
    top: 247px;
    width: 28px;
    height: 28px;
    border-radius: 50%;
    background: var(--gold);
  }
  .brand-name {
    left: 108px;
    width: 300px;
    top: 352px;
    font-family: "Inconsolata", monospace;
    font-weight: 500;
    font-size: 40px;
    line-height: 56px;
    letter-spacing: 0.22em;
    text-transform: uppercase;
    color: var(--ink);
  }
  .effect-list {
    left: 108px;
    width: 300px;
    font-family: "Inconsolata", monospace;
    font-size: 27px;
    line-height: 32px;
    letter-spacing: 0.16em;
    text-transform: uppercase;
    color: var(--gold);
  }
  .effect-list p { margin: 0 0 32px; }
  /* back */
  .back-title {
    left: 624px;
    width: 300px;
    top: 259px;
    font-family: "Open Sans", sans-serif;
    font-size: 28px;
    line-height: 38px;
    color: var(--ink);
  }
  .effect-copy {
    left: 604px;
    width: 340px;
    font-family: "Open Sans", sans-serif;
    font-size: 15.5px;
    line-height: 22.4px;
    color: var(--ink);
  }
  .effect-copy h3 {
    margin: 0;
    font-size: 16.5px;
    font-weight: 700;
  }
  .effect-copy p { margin: 0; }
  .ean-box {
    position: absolute;
    left: 635px;
    top: 775px;
    width: 271px;
    height: 116px;
    border: 1px solid #555;
    box-sizing: border-box;
    font-family: "Open Sans", sans-serif;
    font-size: 16px;
    color: var(--ink);
    text-align: center;
  }
  .ean-box span {
    position: absolute;
    left: 0;
    right: 0;
    bottom: 10px;
  }
  .imprint {
    left: 620px;
    width: 300px;
    top: 904px;
    font-family: "Open Sans", sans-serif;
    font-size: 13.5px;
    line-height: 19.3px;
    color: var(--ink);
  }
</style>
</head>
<body>
<div class="canvas">
  <svg class="tube-shapes" width="1049" height="1200" viewBox="0 0 1049 1200" aria-hidden="true">
    <!-- front tube -->
    <path d="M27 39 H489 L405 984 H108 Z" fill="var(--tube)" stroke="var(--tube-edge)"/>
    <rect x="27" y="39" width="462" height="40" fill="#f0f0f0"/>
    <path d="M108 984 H405 L403 1160 Q256 1186 111 1160 Z" fill="var(--cap)" stroke="var(--tube-edge)"/>
    <path d="M108 981 Q256 1004 405 981 L405 996 Q256 1021 108 996 Z" fill="var(--gold)"/>
    <!-- back tube -->
    <path d="M543 39 H1005 L923 984 H626 Z" fill="var(--tube)" stroke="var(--tube-edge)"/>
    <rect x="543" y="39" width="462" height="40" fill="#f0f0f0"/>
    <path d="M626 984 H923 L921 1160 Q774 1186 629 1160 Z" fill="var(--cap)" stroke="var(--tube-edge)"/>
    <path d="M626 985 Q774 1008 923 985 L923 1000 Q774 1025 626 1000 Z" fill="var(--gold)"/>
  </svg>

  <!-- front -->
  <span class="brand-dot"></span>
  <h1 class="block brand-name">Soleva<br>Amarin</h1>
  <div class="block effect-list" style="top:505px;">
    <p>Volume<br>Effect</p>
    <p>Detox<br>Effect</p>
    <p>Firming<br>Effect</p>
  </div>

  <!-- back -->
  <h2 class="block back-title" style="font-weight:400;">Der Dreifach<br>Wirkkomplex</h2>
  <section class="block effect-copy" style="top:366px;">
    <h3>VOLUME-EFFECT</h3>
    <p>Stimuliert die Adipozyten-<br>differenzierung, damit<br>funktionsfähige Adipozyten entstehen.<br>Positiver Effekt auf Volumen.</p>
  </section>
  <section class="block effect-copy" style="top:500px;">
    <h3>DETOX-EFFECT</h3>
    <p>Tessalin aktiviert Proteasome 20S,<br>die beschädigte Zellen beseitigt und<br>so die Zelltoxizität herabsetzt.</p>
  </section>
  <section class="block effect-copy" style="top:612px;">
    <h3>FIRMING-EFFECT</h3>
    <p>Steigert die Dynamik der Fibrolasten<br>um die Matrix wechselwirkungen<br>wiederherzustellen.</p>
  </section>
  <div class="ean-box"><span>Barcode 4019283746512</span></div>
  <p class="block imprint">Made in Germany<br>Kelbrand GmbH - Anton-Feiler-Str. 7<br>34567 Musterdorf</p>
</div>
</body>
</html>
```